Sports Psychology Business Card Design

Need a catchy and unique business card design for our sport psychology practice. We provide mental performance counseling and consulting to performers from all types of industries with a special emphases on athletes.The name of our practice is "Steady Core of Achievement" or "SCA" as is indicated in the logo examples submitted in this brief. Also provided were logos with specific sports referenced which represent sources of our clients from those sports.

Target Market(s)

Executives, Professionals (doctors, lawyers, etc.), Athletes, Entertainers and other performers

Contact Information for Business Card

Need to include our logo (logos provided in this brief).

Font styles to use
Other font styles liked:
• Font can be found in logo

Colors
0792cd
34a7d8
85cae6

Requirements
Must have
• Our logo and reference to our provision of mental performance counseling/consulting/coaching
Nice to have
• References to sports that our athletes play as provided in the brief.
Should not have
• This is not a general wellness consulting practice. Our focus is on consulting to improve mental performance.

```html
<!DOCTYPE html>
<html lang="en">
<head>
<meta charset="utf-8">
<title>Steady Core of Achievement – Business Card</title>
<link href="https://fonts.googleapis.com/css2?family=Source+Sans+3:wght@400;600;700&display=swap" rel="stylesheet">
<style>
  :root {
    --backdrop: #838287;
    --card-light: #ffffff;
    --card-dark: #2b2e32;
    --ink: #2b2e31;
    --brand-blue: #0f72b8;
    --logo-dot: #0792cd;
  }
  * { margin: 0; padding: 0; box-sizing: border-box; }
  html, body {
    width: 1200px; height: 999px; overflow: hidden;
    background: var(--backdrop);
    font-family: "Source Sans 3", "Myriad Pro", Arial, sans-serif;
  }
  .canvas { position: relative; width: 1200px; height: 999px; }

  .card { position: absolute; width: 791px; height: 452px; }
  .card--front { left: 94px; top: 43px; background: var(--card-light); }
  .card--back { left: 265px; top: 526px; background: var(--card-dark); }

  .wordmark {
    position: absolute; display: flex; align-items: center; gap: 14px;
    font-weight: 700; font-size: 64px; letter-spacing: 6px; line-height: 1;
  }
  .wordmark__dot {
    width: 18px; height: 18px; border-radius: 50%; background: var(--logo-dot);
  }
  .card--front .wordmark { left: 330px; top: 86px; color: var(--ink); }
  .card--back .wordmark { left: 330px; top: 192px; color: #ffffff; }

  .holder { position: absolute; left: 51px; top: 248px; }
  .holder__name { color: var(--brand-blue); font-weight: 700; font-size: 31px; line-height: 1; }
  .holder__role { color: var(--ink); font-size: 18px; margin-top: 12px; }

  .divider { position: absolute; left: 0; top: 329px; width: 100%; height: 5px; background: var(--ink); }

  .address {
    position: absolute; left: 51px; top: 349px;
    color: var(--ink); font-size: 19px; line-height: 24px;
  }
  .contacts { position: absolute; left: 520px; top: 349px; list-style: none; }
  .contacts li {
    display: flex; align-items: center; gap: 16px;
    color: var(--ink); font-size: 19px; line-height: 24.5px;
  }
  .contacts svg { width: 20px; height: 20px; fill: var(--ink); }
</style>
</head>
<body>
<div class="canvas">

  <section class="card card--front">
    <div class="wordmark"><span>SCA</span><span class="wordmark__dot"></span></div>

    <div class="holder">
      <p class="holder__name">Name Title</p>
      <p class="holder__role">designation</p>
    </div>

    <div class="divider"></div>

    <p class="address">suit # 00, Lorem ipsum<br>Lorem Lorem ipsum</p>

    <ul class="contacts">
      <li>
        <svg viewBox="0 0 24 24" aria-hidden="true"><path d="M6.6 10.8a15.1 15.1 0 0 0 6.6 6.6l2.2-2.2a1 1 0 0 1 1-.25 11.4 11.4 0 0 0 3.6.57 1 1 0 0 1 1 1V20a1 1 0 0 1-1 1A17 17 0 0 1 3 4a1 1 0 0 1 1-1h3.5a1 1 0 0 1 1 1c0 1.25.2 2.45.57 3.6a1 1 0 0 1-.25 1z"/></svg>
        000-000-0000
      </li>
      <li>
        <svg viewBox="0 0 24 24" aria-hidden="true"><path d="M12 2 2 9v12h20V9L12 2zm0 2.4 7.6 5.3L12 14 4.4 9.7 12 4.4z"/></svg>
        abcde@steadycore.com
      </li>
      <li>
        <svg viewBox="0 0 24 24" aria-hidden="true"><path d="M12 2a10 10 0 1 0 0 20 10 10 0 0 0 0-20zm6.9 6h-3a15.6 15.6 0 0 0-1.4-3.9A8 8 0 0 1 18.9 8zM12 4c.8 1.2 1.5 2.5 1.9 4h-3.8c.4-1.5 1.1-2.8 1.9-4zM4.3 14a8.2 8.2 0 0 1 0-4h3.4a16 16 0 0 0 0 4zm.8 2h3a15.6 15.6 0 0 0 1.4 3.9A8 8 0 0 1 5.1 16zm3-8h-3a8 8 0 0 1 4.4-3.9A15.6 15.6 0 0 0 8.1 8zM12 20c-.8-1.2-1.5-2.5-1.9-4h3.8c-.4 1.5-1.1 2.8-1.9 4zm2.3-6H9.7a14.4 14.4 0 0 1 0-4h4.6a14.4 14.4 0 0 1 0 4zm.2 5.9A15.6 15.6 0 0 0 15.9 16h3a8 8 0 0 1-4.4 3.9zm1.8-5.9a16 16 0 0 0 0-4h3.4a8.2 8.2 0 0 1 0 4z"/></svg>
        www.steadycore.com
      </li>
    </ul>
  </section>

  <section class="card card--back">
    <div class="wordmark"><span>SCA</span><span class="wordmark__dot"></span></div>
  </section>

</div>
</body>
</html>
```